Webdesign für Rheinau Vita Forschungsbund e.V.
Zielgruppe
Vereinsmitglieder aus der Bio-Tech-Branche, Öffentlichkeit
Aufgabenstellung
Wir benötigen ein Webdesign für die Website des Rheinau Vita Forschungsbund e.V., zu liefern als PSD-Datei.

```html
<!DOCTYPE html>
<html lang="de">
<head>
<meta charset="utf-8">
<title>Rheinau Vita Forschungsbund</title>
<link href="https://fonts.googleapis.com/css2?family=Arimo:ital,wght@0,400;0,700;1,700&display=swap" rel="stylesheet">
<style>
:root{
  --navy:#0c4a6e;
  --sky:#93c9d8;
  --teal:#3f8fa3;
  --teal-dark:#2d6b7c;
  --wine:#5a0b0b;
  --text:#2a2a2a;
  --link-red:#c0221e;
  --green-head:#0d4a3a;
  --aqua:#5cc8c2;
  --blue-copy:#2275b8;
  --page:#f4f8fa;
  --hero-warm:#f2c46a;
  --hero-light:#f5dc9c;
  --hero-cool:#9ccf86;
}
*{box-sizing:border-box;margin:0;padding:0}
html,body{width:1170px;height:1200px;overflow:hidden;background:var(--page);font-family:"Arimo",Arial,sans-serif;color:var(--text)}
.canvas{position:relative;width:1170px;height:1200px}
.bar-dark{position:absolute;left:39px;width:1092px;height:12px;background:var(--navy)}
.bar-light{position:absolute;left:39px;width:1092px;background:var(--sky)}
.logo-tab{position:absolute;left:450px;top:0;width:322px;height:160px;background:#fff;border-radius:0 0 14px 14px;box-shadow:0 2px 6px rgba(0,0,0,.15);display:flex;flex-direction:column;align-items:center;justify-content:flex-end;padding-bottom:48px;z-index:2}
.logo-dot{width:48px;height:48px;border-radius:50%;background:var(--teal);margin-bottom:14px}
.logo-name{font-size:14px;font-weight:700;letter-spacing:1.5px;color:#333;text-transform:uppercase}
.hero{position:absolute;left:39px;top:130px;width:1092px;height:525px;
  background:linear-gradient(100deg,var(--hero-light) 0%,var(--hero-warm) 45%,var(--hero-cool) 100%)}
.tagline{position:absolute;right:12px;bottom:32px;text-align:right;color:#fff;font-weight:700;text-shadow:0 1px 4px rgba(0,0,0,.55)}
.tagline .small{font-size:18px;font-weight:400}
.tagline .big{font-size:31px}
.tagline .line2{font-size:27px;display:block;margin-top:2px}
.nav{position:absolute;left:39px;width:183px;height:52px;background:linear-gradient(#5aa8b8,var(--teal-dark));color:#fff;font-size:15px;display:flex;align-items:center;padding-left:43px;box-shadow:0 1px 2px rgba(0,0,0,.3)}
.nav.active{background:linear-gradient(#d8d8d8,#a8a8a8);color:#222}
.box{position:absolute;top:679px;width:256px;height:429px;background:#fff;border:1px solid #2d3b4a;border-radius:8px;overflow:hidden}
.box-head{height:55px;color:#fff;font-size:20px;display:flex;align-items:center;padding-left:18px}
.news .box-head{background:var(--sky)}
.news-item{height:124px;border-bottom:1px solid #2d3b4a;padding:16px 14px 0 16px;position:relative}
.news-item:last-child{border-bottom:none}
.news-item h3{font-size:14px;color:var(--green-head);text-decoration:underline;margin-bottom:8px}
.news-item p{font-size:13px;line-height:16px}
.more-red{position:absolute;right:12px;bottom:12px;font-size:10px;color:var(--link-red);text-decoration:underline}
.events .box-head{background:var(--wine);height:52px}
.event{height:155px;padding:26px 22px 0 22px;border-bottom:1px solid #2d3b4a}
.event:last-child{border-bottom:none}
.event .date{font-size:11px;font-weight:700}
.event h3{font-size:16px;color:var(--aqua);margin:5px 0 9px}
.event p{font-size:11px;line-height:14px}
.event .more{font-size:10px;color:var(--aqua);text-decoration:underline;display:block;margin-top:14px}
.welcome{position:absolute;left:336px;top:690px;width:510px}
.welcome h1{font-size:23px;font-style:italic;font-weight:700;color:var(--navy)}
.dots{border-bottom:2px dotted #9ab;width:415px;margin:14px 0 28px}
.welcome p{font-size:15px;line-height:19px;color:var(--blue-copy)}
.welcome p+p{margin-top:19px}
.thumb{position:absolute;top:966px;width:156px;height:105px}
.footer-bar{position:absolute;left:39px;top:1138px;width:1092px;height:30px;background:var(--sky);font-size:9px;display:flex;align-items:center;padding:0 16px}
.footer-bar a{margin-right:27px;color:#333;text-decoration:none}
.footer-bar .copy{margin-left:auto}
</style>
</head>
<body>
<div class="canvas">
  <div class="bar-dark" style="top:73px"></div>
  <div class="bar-light" style="top:89px;height:29px"></div>
  <div class="logo-tab"><span class="logo-dot"></span><span class="logo-name">Rheinau Vita Forschungsbund</span></div>

  <div class="hero" role="img" aria-label="Foto: Laborkolben mit farbigen Flüssigkeiten">
    <div class="tagline"><span class="small">Der </span><span class="big">Schrittmacher</span><span class="small"> für die</span><span class="line2">Biotechnologie-Region Rhein-Main</span></div>
  </div>

  <nav>
    <a class="nav active" style="top:154px">Startseite</a>
    <a class="nav" style="top:225px">Über Uns</a>
    <a class="nav" style="top:294px">Veranstaltungen</a>
    <a class="nav" style="top:369px">Aktuelles</a>
    <a class="nav" style="top:440px">Region</a>
    <a class="nav" style="top:505px">Service</a>
    <a class="nav" style="top:573px">Kontakt</a>
  </nav>

  <section class="box news" style="left:39px">
    <div class="box-head">Aktuelles</div>
    <article class="news-item"><h3>Neue Spezies entdeckt</h3><p>Lorem ipsum dolor sit amet,<br>consectetur adipiscing elit.<br>Nullam elementum varius</p><span class="more-red">mehr Informationen</span></article>
    <article class="news-item"><h3>Neue Spezies entdeckt</h3><p>Lorem ipsum dolor sit amet,<br>consectetur adipiscing elit.<br>Nullam elementum varius</p><span class="more-red">mehr Informationen</span></article>
    <article class="news-item"><h3>Neue Spezies entdeckt</h3><p>Lorem ipsum dolor sit amet,<br>consectetur adipiscing elit.<br>Nullam elementum varius</p><span class="more-red">mehr Informationen</span></article>
  </section>

  <main class="welcome">
    <h1>Herzlich Willkommen</h1>
    <div class="dots"></div>
    <p>Der Rheinau Vita Forschungsbund versteht sich als Schrittmacher für die Biotechnologie-Region Rhein-Main. Wir sind qualifizierter Ansprech&shy;partner für Unternehmen, Politik und Medien und Interessenvertretung für alle, die in derWertschöpfungskette von der Grundlagenforschung bis zum fertigen Produkt und seiner Vermarktung arbeiten.</p>
    <p>Hierfür bieten wir ein in der Region einzigartiges Netzwerk.</p>
    <div class="dots" style="margin-top:22px"></div>
  </main>
  <div class="thumb" style="left:336px;background:linear-gradient(#e8eef4,#b8c8da)" role="img" aria-label="Foto: Probenfläschchen im Labor"></div>
  <div class="thumb" style="left:508px;background:linear-gradient(#c8ccd0,#6a6e72)" role="img" aria-label="Foto: Mikroskop"></div>
  <div class="thumb" style="left:681px;background:linear-gradient(#9cc84a,#5e9a2a)" role="img" aria-label="Foto: grüne Zellen"></div>

  <section class="box events" style="left:876px">
    <div class="box-head">Veranstaltungen</div>
    <article class="event"><div class="date">20.12.10</div><h3>Escherichia Coli</h3><p>Hier steht eine kurze Beschreibung<br>zum Thema und dann ein Link<br>zum aufrufen der Veranstaltung</p><span class="more">mehr Informationen</span></article>
    <article class="event"><div class="date">20.12.10</div><h3>Escherichia Coli</h3><p>Hier steht eine kurze Beschreibung<br>zum Thema und dann ein Link<br>zum aufrufen der Veranstaltung</p><span class="more">mehr Informationen</span></article>
  </section>

  <footer class="footer-bar">
    <a>Über Uns</a><a>Veranstaltungen</a><a>Aktuelles</a><a>Region</a><a>Service</a>
    <span class="copy">© 2011 RHEINAU VITA FORSCHUNGSBUND</span>
  </footer>
  <div class="bar-dark" style="top:1173px"></div>
</div>
</body>
</html>
```